Brookmere Osteopathy flyer

I want a clean clear DL flyer (but also want an A4 poster) promoting a new Osteopathic business in a semi rural area in Tasmania (Australia).
It can have pictures like the examples attached to show people what Osteopathy is (its like Chiropractic and physiotherapy).
I am the sole practioner and am male, so any pictures would be best to be a white male if possible.
I've attached some wording, you can use all, or none of it
I don't have a phone number for the business yet
info@brookmereosteopathy.example
www.brookmereosteopathy.example
Target Market(s)
Australians, from tradies, professionals, babies to retired people
Industry/Entity Type
Health
Look and feel

```html
<!DOCTYPE html>
<html lang="en">
<head>
<meta charset="utf-8">
<title>Brookmere Osteopathy – Flyer</title>
<link href="https://fonts.googleapis.com/css2?family=Outfit:wght@600&family=Cabin:wght@400;600&display=swap" rel="stylesheet">
<style>
  :root {
    --orange: #f7923a;
    --blue: #0f98d3;
    --sky: #dcf0fb;
    --ink: #0d0d0d;
    --white: #ffffff;
  }
  * { margin: 0; padding: 0; box-sizing: border-box; }
  html, body { width: 900px; height: 1200px; overflow: hidden; background: var(--white); }
  .flyer { position: relative; width: 900px; height: 1200px; overflow: hidden; background: var(--white); font-family: "Cabin", sans-serif; }
  .flyer-shapes { position: absolute; inset: 0; }

  .headline {
    position: absolute; right: 71px; top: 604px; text-align: right;
    font-family: "Outfit", sans-serif; font-weight: 600; font-size: 37px;
    line-height: 44px; color: var(--ink); letter-spacing: -0.3px;
  }
  .headline-rule { position: absolute; left: 0; top: 660px; width: 375px; height: 6px; background: var(--orange); }

  .reasons { list-style: none; }
  .reasons li {
    position: absolute; display: flex; align-items: center; width: 340px; height: 64px;
    font-size: 20px; color: var(--ink); line-height: 1.25;
  }
  .reasons li.reason-small { font-size: 17px; }
  .reason-icon {
    flex: none; display: flex; align-items: center; justify-content: center;
    width: 54px; height: 54px; border-radius: 50%; background: var(--orange);
    box-shadow: 0 0 0 3px var(--white), 0 0 0 4px var(--blue); margin-right: 23px;
  }
  .reason-icon svg { width: 28px; height: 28px; fill: none; stroke: var(--white); stroke-width: 1.6; stroke-linecap: round; stroke-linejoin: round; }

  .method-band {
    position: absolute; left: 0; top: 1054px; width: 687px; height: 80px; background: var(--blue);
    color: var(--white); font-weight: 600; font-size: 14.5px; line-height: 16.5px; padding: 15px 0 0 42px;
  }
  .method-band p { width: 430px; }

  .contact-band { position: absolute; left: 0; top: 1134px; width: 900px; height: 66px; background: var(--orange); color: var(--white); font-size: 13.5px; }
  .contact-col { position: absolute; line-height: 18px; }
  .contact-col.left { left: 42px; top: 24px; }
  .contact-col.right { left: 376px; top: 14px; }
  .contact-line { display: flex; align-items: center; gap: 5px; }
  .contact-line svg { width: 10px; height: 10px; }

  .brand-seal {
    position: absolute; left: 638px; top: 1012px; width: 280px; height: 280px; border-radius: 50%;
    background: var(--sky); border: 8px solid var(--white);
  }
  .brand-name {
    position: absolute; left: 660px; top: 1090px; width: 230px; text-align: center;
    font-weight: 600; font-size: 19px; line-height: 24px; color: var(--blue);
  }
</style>
</head>
<body>
<main class="flyer">
  <svg class="flyer-shapes" width="900" height="1200" viewBox="0 0 900 1200">
    <defs>
      <linearGradient id="treatmentTone" x1="0" y1="0" x2="0.6" y2="1">
        <stop offset="0" stop-color="#eef1f3"/>
        <stop offset="0.45" stop-color="#d3e6f1"/>
        <stop offset="0.8" stop-color="#8cc6ea"/>
        <stop offset="1" stop-color="#5fb2e4"/>
      </linearGradient>
      <linearGradient id="portraitTone" x1="0" y1="0" x2="0.4" y2="1">
        <stop offset="0" stop-color="#a9c7d4"/>
        <stop offset="0.55" stop-color="#d6e4ec"/>
        <stop offset="1" stop-color="#eef4f7"/>
      </linearGradient>
    </defs>
    <path role="img" aria-label="Photo of an osteopath stretching a patient's shoulder on a treatment table"
      d="M0 0 H790 C768 180 650 330 440 385 C280 430 120 438 0 420 Z" fill="url(#treatmentTone)"/>
    <path class="swoosh-blue-top" d="M840 0 H900 V335 C860 380 800 410 700 430 L690 400 C770 330 830 200 840 0 Z" fill="var(--blue)"/>
    <path class="swoosh-orange" d="M790 0 H846 C830 210 700 390 450 468 C300 512 140 528 0 520 V420 C120 438 280 430 440 385 C650 330 768 180 790 0 Z" fill="var(--orange)"/>
    <path class="swoosh-blue-low" d="M82 574 C250 562 400 532 520 472 L545 535 C400 568 250 578 82 574 Z" fill="var(--blue)"/>
    <circle role="img" aria-label="Portrait photo of the practitioner in a white coat with arms crossed"
      cx="657" cy="405" r="200" fill="url(#portraitTone)" stroke="var(--white)" stroke-width="7"/>
  </svg>

  <h1 class="headline">COMMON REASONS PEOPLE<br>VISIT AN OSTEOPATH</h1>
  <div class="headline-rule"></div>

  <ul class="reasons">
    <li style="left:71px;top:700px"><span class="reason-icon"><svg viewBox="0 0 28 28"><rect x="11" y="3" width="6" height="4" rx="1.5"/><rect x="11" y="9" width="6" height="4" rx="1.5"/><rect x="11" y="15" width="6" height="4" rx="1.5"/><rect x="11" y="21" width="6" height="4" rx="1.5"/></svg></span>Back / neck pain</li>
    <li style="left:71px;top:769px"><span class="reason-icon"><svg viewBox="0 0 28 28"><path d="M16 3 L9 15 H14 L12 25 L20 12 H15 Z"/></svg></span>Headaches / migraines</li>
    <li style="left:71px;top:838px"><span class="reason-icon"><svg viewBox="0 0 28 28"><circle cx="14" cy="14" r="5"/><path d="M14 3 V8 M14 20 V25 M3 14 H8 M20 14 H25"/></svg></span>Joint and muscle pain</li>
    <li style="left:71px;top:907px;width:400px"><span class="reason-icon"><svg viewBox="0 0 28 28"><path d="M14 23 C6 17 4 13 4 10 A5 5 0 0 1 14 8 A5 5 0 0 1 24 10 C24 13 22 17 14 23 Z"/></svg></span>Pregnancy-related discomfort</li>
    <li style="left:71px;top:976px"><span class="reason-icon"><svg viewBox="0 0 28 28"><ellipse cx="14" cy="9" rx="9" ry="3.5"/><path d="M5 9 V19 A9 3.5 0 0 0 23 19 V9"/></svg></span>Disc related issues</li>
    <li style="left:495px;top:700px"><span class="reason-icon"><svg viewBox="0 0 28 28"><path d="M14 3 L10 9 L17 13 L10 18 L15 25"/></svg></span>Sciatica</li>
    <li style="left:495px;top:769px"><span class="reason-icon"><svg viewBox="0 0 28 28"><path d="M4 18 C9 12 12 22 17 16 S24 12 24 12 M4 23 H24"/></svg></span>Plantar fasciitis</li>
    <li style="left:495px;top:838px" class="reason-small"><span class="reason-icon"><svg viewBox="0 0 28 28"><path d="M14 3 V10 M14 18 V25"/><circle cx="14" cy="14" r="4"/><path d="M8 8 L10 10 M20 8 L18 10"/></svg></span>Tendonitis / Bursitis</li>
    <li style="left:495px;top:907px"><span class="reason-icon"><svg viewBox="0 0 28 28"><path d="M4 22 C4 12 10 8 16 8 H24"/><circle cx="14" cy="10" r="3"/></svg></span>Adhesive capsulitis<br>(frozen shoulder)</li>
    <li style="left:495px;top:976px"><span class="reason-icon"><svg viewBox="0 0 28 28"><path d="M4 8 L14 18 L24 10"/><circle cx="14" cy="18" r="2.5"/></svg></span>Tennis / Golfers elbow</li>
  </ul>

  <section class="method-band">
    <p>Osteopaths use a combination of joint manipulation, targeted deep tissue massage and stretching to improve function, relieve pain and support the body’s ability to heal itself.</p>
  </section>

  <footer class="contact-band">
    <div class="contact-col left">
      <div class="contact-line"><svg viewBox="0 0 10 10"><path fill="var(--white)" d="M5 0 A3.5 3.5 0 0 1 8.5 3.5 C8.5 6 5 10 5 10 C5 10 1.5 6 1.5 3.5 A3.5 3.5 0 0 1 5 0 Z M5 2.2 A1.3 1.3 0 1 0 5 4.8 A1.3 1.3 0 1 0 5 2.2 Z" fill-rule="evenodd"/></svg>42 Mill Creek Road, Brookmere</div>
    </div>
    <div class="contact-col right">
      <div class="contact-line"><svg viewBox="0 0 10 10" fill="none" stroke="var(--white)" stroke-width="0.9"><circle cx="5" cy="5" r="4.2"/><ellipse cx="5" cy="5" rx="1.8" ry="4.2"/><path d="M0.8 5 H9.2"/></svg>www.brookmereosteopathy.example</div>
      <div class="contact-line"><svg viewBox="0 0 10 10"><rect x="0.5" y="2" width="9" height="6" fill="var(--white)"/><path d="M1.2 2.6 L5 5.4 L8.8 2.6" fill="none" stroke="var(--orange)" stroke-width="0.8"/></svg>info@brookmereosteopathy.example</div>
    </div>
  </footer>

  <div class="brand-seal"></div>
  <p class="brand-name">Brookmere<br>Osteopathy</p>
</main>
</body>
</html>
```